Redesign wellness clinic website

The project is redesign a wellness clinic http://www.ambermoorwellness.example. The new website is to be responsive,clean,bright and a strong call to action which is to book an appointment. The logo will remain the same but the colour scheme on the website should be reflect purple white and green. I want it to be bright and cheerful and the feeling of clarity. The website shouldn't be overloaded with content but more visuals.

Target Market(s)

Anyone that has corporate wellness benefits within the downtown Toronto core. Majority of audience are professional working in Media, Telecommunications and Investments.

Industry/Entity Type

Health And Wellness

Number of Pages Required

5+ page

Font styles to use
Sans Serif

Colors
ffffff
886aae
acd036

Requirements
Must have
• -Strong call to action which is book an appointment like this page https://www.kestrelphysio.example/
• -Services provided icons on the page like https://www.brightpathhealthstudio.example/
• - Pictures of a good visualizing a fit and healthy life
• - Strong ratings from Rendo, Vastly, CityPin, similar to this website http://www.summitcrestclinic.example/our-team-professionals/
• - Bright and clear
Should not have
• -No black and white images (redo our pictures)
• -Dark themes

```html
<!DOCTYPE html>
<html lang="en">
<head>
<meta charset="utf-8">
<title>Ambermoor Wellness Centre</title>
<link rel="stylesheet" href="https://fonts.googleapis.com/css2?family=Lato:wght@400;700&family=Open+Sans:ital,wght@0,400;0,600;0,700;1,400&display=swap">
<style>
:root{
  --purple:#886aae;
  --purple-deep:#7a3a8f;
  --purple-soft:#a58bc6;
  --green:#acd036;
  --green-deep:#93b82c;
  --green-dark:#85a626;
  --white:#ffffff;
  --ink:#3a3a3a;
  --muted:#777777;
  --grey-bg:#efefef;
}
*{box-sizing:border-box;margin:0;padding:0}
html,body{width:1200px;height:3495px;overflow:hidden}
body{position:relative;background:var(--white);font-family:"Open Sans",Arial,sans-serif;color:var(--ink)}
.abs{position:absolute}

/* header */
.site-header{left:0;top:0;width:1200px;height:105px;background:var(--white);box-shadow:0 2px 6px rgba(0,0,0,.08);z-index:5}
.brand{left:125px;top:20px;display:flex;align-items:center;gap:10px}
.brand-dot{width:60px;height:60px;border-radius:50%;background:var(--green);flex:none}
.brand-name{font-size:17px;font-weight:600;color:var(--purple-deep);white-space:nowrap}
.main-nav{left:477px;top:40px;display:flex;gap:22px;font-size:14px;white-space:nowrap}
.main-nav a{color:#555;text-decoration:none}
.main-nav a.active{color:var(--purple-deep)}

/* hero */
.hero{left:0;top:105px;width:1200px;height:560px;background:linear-gradient(100deg,#8b5fb0 0%,#b08bc5 45%,#c9d48a 80%,#b6d15a 100%)}
.hero-title{left:0;width:1200px;top:165px;text-align:center;color:var(--white);font-size:41px;font-weight:600}
.hero-sub{left:0;width:1200px;top:225px;text-align:center;color:var(--white);font-size:18px;line-height:26px;font-weight:600}
.hero-cta{left:454px;top:295px;width:278px;height:50px;border:2px solid var(--white);color:var(--white);font-size:15px;font-weight:600;letter-spacing:.5px;display:flex;align-items:center;justify-content:center}
.hero-arrow{top:205px;width:50px;height:74px;background:#333;display:flex;align-items:center;justify-content:center}
.hero-arrow.left{left:-10px;border-radius:0 37px 37px 0}
.hero-arrow.right{right:-10px;border-radius:37px 0 0 37px}
.hero-curve{left:0;top:510px}

/* services */
.section-title{left:0;width:1200px;text-align:center;font-family:"Lato",sans-serif;font-size:28px;font-weight:400;color:#555;letter-spacing:1px}
.section-title span::before,.section-title span::after{content:"";display:inline-block;width:40px;height:1px;background:#999;vertical-align:middle;margin:0 16px}
.service{width:240px;text-align:center}
.service-icon{width:145px;height:145px;border-radius:50%;margin:0 auto}
.service-icon.green{background:var(--green)}
.service-icon.purple{background:var(--purple)}
.service-name{margin-top:22px;font-size:16px;font-weight:700;color:#444}
.service-text{margin-top:8px;font-size:12px;line-height:18px;color:var(--muted)}
.chev{top:815px}
.services-curve{left:0;top:1020px}

/* welcome */
.welcome-photo{left:140px;top:1095px;width:382px;height:382px;border-radius:50%;background:linear-gradient(160deg,#cfe3f0 0%,#8fb9d6 55%,#6d8a9c 100%)}
.welcome-title{left:592px;top:1152px;font-family:"Lato",sans-serif;font-size:32px;font-weight:400;color:#444}
.welcome-body{left:592px;top:1210px;width:470px;font-size:15px;line-height:26px;color:#555}
.welcome-body p+p{margin-top:12px}
.btn{display:flex;align-items:center;justify-content:center;color:var(--white);font-size:13px;font-weight:700;letter-spacing:.5px}
.btn-purple{left:592px;top:1412px;width:161px;height:42px;background:var(--purple)}

/* video */
.video-band{left:0;top:1526px;width:1200px;height:450px;background:var(--grey-bg)}
.video-title{left:128px;top:1620px;font-family:"Lato",sans-serif;font-size:34px;font-weight:400;color:#444}
.video-body{left:130px;top:1678px;width:470px;font-size:15px;line-height:25px;color:#555}
.btn-green{left:133px;top:1845px;width:158px;height:40px;background:var(--green)}
.video-frame{left:599px;top:1596px;width:478px;height:303px;background:linear-gradient(120deg,#d9dde0 0%,#9fb1bd 60%,#7a8c98 100%);box-shadow:0 2px 8px rgba(0,0,0,.25)}
.play{left:191px;top:103px}

/* testimonials */
.testi-mark{left:576px;top:1995px;width:48px;height:48px;border-radius:50%;background:var(--green)}
.testi-title{left:0;width:1200px;top:2052px;text-align:center;font-family:"Lato",sans-serif;font-size:32px;font-weight:700;color:var(--purple-deep)}
.testi-quote{left:230px;top:2112px;width:740px;text-align:center;font-style:italic;font-size:14px;line-height:29px;color:#555}
.qmark{font-family:Georgia,serif;font-size:56px;color:var(--purple-deep);font-style:normal;font-weight:700}
.qmark.open{left:205px;top:2090px}
.qmark.close{left:888px;top:2160px}
.testi-name{left:0;width:1200px;top:2232px;text-align:center;font-size:14px;font-weight:700;color:#444}
.testi-company{left:0;width:1200px;top:2256px;text-align:center;font-size:12px;color:#555}
.dots{left:570px;top:2306px;display:flex;gap:7px}
.dots i{width:10px;height:10px;border-radius:50%;background:#aaa}
.dots i:first-child{background:#fff;border:1px solid #888}

/* blogs */
.blogs{left:0;top:2365px;width:1200px;height:506px;background:linear-gradient(160deg,#8c64b0 0%,#a888b8 35%,#b4c16c 70%,#a8cf35 100%)}
.blogs-title{left:0;width:1200px;top:24px;text-align:center;font-family:"Lato",sans-serif;font-size:32px;font-weight:400;color:var(--white)}
.blog{width:300px;text-align:center;color:var(--white)}
.blog-photo{width:176px;height:176px;border-radius:50%;border:4px solid var(--white);margin:0 auto}
.blog-title{margin-top:12px;font-size:17px;font-weight:700;line-height:22px}
.blog-text{margin-top:8px;font-size:10px;line-height:14px}
.blog-more{margin-top:12px;font-size:11px;font-weight:700}
.blogs-btn{left:482px;top:422px;width:233px;height:44px;border:2px solid var(--white);color:var(--white);font-size:13px;font-weight:700;display:flex;align-items:center;justify-content:center}

/* ratings */
.rating{top:2940px;width:263px;height:103px;border-radius:52px;background:var(--white);border:2px solid #ddd;box-shadow:0 3px 6px rgba(0,0,0,.12);display:flex;flex-direction:column;align-items:center;justify-content:center;gap:8px}
.rating-name{font-size:30px;font-weight:700;color:#555}
.stars{display:flex;gap:4px}
.star{width:18px;height:18px}

/* footer */
.footer-curve{left:0;top:2995px}
.footer{left:0;top:3080px;width:1200px;height:345px;background:var(--green)}
.footer-col{top:100px;color:var(--white);font-size:12px}
.footer-col h4{font-size:13px;font-weight:700;margin-bottom:16px}
.footer-col li{list-style:none;line-height:29px;display:flex;align-items:center;gap:6px;white-space:nowrap}
.footer-col .org{font-weight:700}
.ficon{width:20px;height:20px;flex:none}
.social{display:flex;gap:14px;margin-top:18px}
.social i{width:16px;height:16px;border-radius:50%;background:var(--white)}
.copyright{left:0;top:3425px;width:1200px;height:70px;background:var(--green-dark);color:#e7f1c8;font-size:11px;display:flex;align-items:center;justify-content:center}
</style>
</head>
<body>

<header class="abs site-header">
  <div class="abs brand"><span class="brand-dot"></span><span class="brand-name">Ambermoor Wellness Centre</span></div>
  <nav class="abs main-nav">
    <a class="active" href="#">Home</a><a href="#">About us</a><a href="#">Services</a><a href="#">Our Staff</a><a href="#">News</a><a href="#">Corporate Wellness</a><a href="#">Contact</a>
  </nav>
</header>

<section class="abs hero" role="img" aria-label="Physiotherapist helping a smiling senior man with a stretching exercise">
  <h1 class="abs hero-title">Physical Therapy &amp; Wellness Centre</h1>
  <p class="abs hero-sub">Our Centre is committed to helping improve and extend the lives of<br>as many people as possible in our community.</p>
  <div class="abs hero-cta">BOOK AN APPOINTMENT &rsaquo;</div>
  <div class="abs hero-arrow left"><svg width="16" height="24" viewBox="0 0 16 24"><path d="M12 3 3 12l9 9" fill="none" stroke="#fff" stroke-width="3"/></svg></div>
  <div class="abs hero-arrow right"><svg width="16" height="24" viewBox="0 0 16 24"><path d="M4 3l9 9-9 9" fill="none" stroke="#fff" stroke-width="3"/></svg></div>
</section>
<svg class="abs hero-curve" width="1200" height="160" viewBox="0 0 1200 160">
  <path d="M0 120 C300 40 700 30 1200 50 L1200 160 L0 160Z" fill="var(--green)"/>
  <path d="M0 140 C300 60 700 45 1200 62 L1200 160 L0 160Z" fill="#fff"/>
</svg>

<h2 class="abs section-title" style="top:680px"><span>OUR SERVICES</span></h2>
<svg class="abs chev" style="left:120px" width="24" height="50" viewBox="0 0 24 50"><path d="M20 2 4 25l16 23" fill="none" stroke="#999" stroke-width="2"/></svg>
<svg class="abs chev" style="left:1054px" width="24" height="50" viewBox="0 0 24 50"><path d="M4 2l16 23-16 23" fill="none" stroke="#999" stroke-width="2"/></svg>
<div class="abs service" style="left:129px;top:750px"><div class="service-icon green" role="img" aria-label="Chiropractic icon"></div><div class="service-name">CHIROPRACTIC</div><div class="service-text">Excepteur sint occaecat<br>cupidatat non proident, sunt<br>in culpa qui</div></div>
<div class="abs service" style="left:337px;top:750px"><div class="service-icon purple" role="img" aria-label="Physiotherapy icon"></div><div class="service-name">PHYSIOTHERAPY</div><div class="service-text">Excepteur sint occaecat cupidatat<br>non proident, sunt in culpa qui</div></div>
<div class="abs service" style="left:560px;top:750px"><div class="service-icon green" role="img" aria-label="Active rehabilitation icon"></div><div class="service-name">ACTIVE REHABILITATION</div><div class="service-text">Excepteur sint occaecat cupidatat<br>non proident, sunt in culpa qui</div></div>
<div class="abs service" style="left:807px;top:750px"><div class="service-icon purple" role="img" aria-label="Massage therapy icon"></div><div class="service-name">MASSAGE THERAPY</div><div class="service-text">Excepteur sint occaecat cupidatat<br>non proident, sunt in culpa qui</div></div>
<svg class="abs services-curve" width="1200" height="80" viewBox="0 0 1200 80">
  <path d="M0 58 C400 70 800 60 1200 12 L1200 40 C800 78 400 80 0 62Z" fill="var(--purple)"/>
</svg>

<div class="abs welcome-photo" role="img" aria-label="Woman meditating in a white outfit on a rock by the sea"></div>
<h2 class="abs welcome-title">Welcome to Our Centre</h2>
<div class="abs welcome-body">
  <p>Established in 1989 the Ambermoor Wellness Centre has become one of Canada's leaders in providing quality care and innovative wellness programs for the community.</p>
  <p>The founder and director Dr. Alan Reeve's vision has come to life with over 30 practitioners providing a multitude of different services under one roof. Some of the services</p>
</div>
<div class="abs btn btn-purple">LEARN MORE</div>

<section class="abs video-band"></section>
<h2 class="abs video-title">Watch Our Video</h2>
<p class="abs video-body">As part of our commitment to serve our community we provide corporate wellness programs &amp; corporate wellness fairs for neighboring corporations. Our wellness fairs include onsite chair massage from a Registered Massage Therapist, Posture checks, presentations and much more.</p>
<div class="abs btn btn-green">LEARN MORE</div>
<div class="abs video-frame" role="img" aria-label="Video still of a therapist treating a man's shoulder">
  <svg class="abs play" width="96" height="96" viewBox="0 0 96 96"><circle cx="48" cy="48" r="44" fill="rgba(255,255,255,.35)" stroke="#fff" stroke-width="5"/><path d="M38 28 68 48 38 68Z" fill="#fff"/></svg>
</div>

<div class="abs testi-mark"></div>
<h2 class="abs testi-title">Testimonials</h2>
<span class="abs qmark open">&ldquo;</span>
<p class="abs testi-quote">Ambermoor Wellness did an amazing Job at Northline Media's Wellness fair. Our team loved learning about the many services offered by Ambermoor's staff, and everyone especially loved the 10 minute massages. They were extremely prepared, organized, and knowledgeable. We look forward to having them back!</p>
<span class="abs qmark close">&rdquo;</span>
<div class="abs testi-name">DANA WHITFIELD,</div>
<div class="abs testi-company">Northline Media</div>
<div class="abs dots"><i></i><i></i><i></i><i></i></div>

<section class="abs blogs">
  <h2 class="abs blogs-title">Ambermoor Blogs</h2>
  <div class="abs blog" style="left:146px;top:90px"><div class="blog-photo" role="img" aria-label="Woman relaxing during a massage" style="background:linear-gradient(135deg,#f2d2b6,#b9835d)"></div><div class="blog-title">Excepteur sint occaecat cupidat<br>non proident sunt</div><div class="blog-text">netus et malesuada fames ac turpis egestas<br>Cras id elit integer quis urna Ut ante</div><div class="blog-more">READ MORE &raquo;</div></div>
  <div class="abs blog" style="left:433px;top:90px"><div class="blog-photo" role="img" aria-label="Wellness blog photo" style="background:linear-gradient(135deg,#f1f1f1,#c9c9c9)"></div><div class="blog-title">Excepteur sint occaecat cupidat<br>non proident sunt</div><div class="blog-text">netus et malesuada fames ac turpis egestas<br>Cras id elit integer quis urna Ut ante</div><div class="blog-more">READ MORE &raquo;</div></div>
  <div class="abs blog" style="left:745px;top:90px"><div class="blog-photo" role="img" aria-label="Therapist assisting a senior patient" style="background:linear-gradient(135deg,#e6eef5,#7fa7cf)"></div><div class="blog-title">Excepteur sint occaecat cupidat<br>non proident sunt</div><div class="blog-text">netus et malesuada fames ac turpis egestas<br>Cras id elit integer quis urna Ut ante</div><div class="blog-more">READ MORE &raquo;</div></div>
  <div class="abs blogs-btn">VIEW MORE BLOGS</div>
</section>

<div class="abs rating" style="left:186px"><span class="rating-name">Rendo</span><div class="stars"><svg class="star" viewBox="0 0 20 20"><path d="M10 1l2.6 6 6.4.5-4.9 4.2 1.5 6.3L10 14.6 4.4 18l1.5-6.3L1 7.5 7.4 7z" fill="#d32323"/></svg><svg class="star" viewBox="0 0 20 20"><path d="M10 1l2.6 6 6.4.5-4.9 4.2 1.5 6.3L10 14.6 4.4 18l1.5-6.3L1 7.5 7.4 7z" fill="#d32323"/></svg><svg class="star" viewBox="0 0 20 20"><path d="M10 1l2.6 6 6.4.5-4.9 4.2 1.5 6.3L10 14.6 4.4 18l1.5-6.3L1 7.5 7.4 7z" fill="#d32323"/></svg><svg class="star" viewBox="0 0 20 20"><path d="M10 1l2.6 6 6.4.5-4.9 4.2 1.5 6.3L10 14.6 4.4 18l1.5-6.3L1 7.5 7.4 7z" fill="#d32323"/></svg><svg class="star" viewBox="0 0 20 20"><path d="M10 1l2.6 6 6.4.5-4.9 4.2 1.5 6.3L10 14.6 4.4 18l1.5-6.3L1 7.5 7.4 7z" fill="#d32323"/></svg></div></div>
<div class="abs rating" style="left:473px"><span class="rating-name">CityPin</span><div class="stars"><svg class="star" viewBox="0 0 20 20"><path d="M10 1l2.6 6 6.4.5-4.9 4.2 1.5 6.3L10 14.6 4.4 18l1.5-6.3L1 7.5 7.4 7z" fill="#d32323"/></svg><svg class="star" viewBox="0 0 20 20"><path d="M10 1l2.6 6 6.4.5-4.9 4.2 1.5 6.3L10 14.6 4.4 18l1.5-6.3L1 7.5 7.4 7z" fill="#d32323"/></svg><svg class="star" viewBox="0 0 20 20"><path d="M10 1l2.6 6 6.4.5-4.9 4.2 1.5 6.3L10 14.6 4.4 18l1.5-6.3L1 7.5 7.4 7z" fill="#d32323"/></svg><svg class="star" viewBox="0 0 20 20"><path d="M10 1l2.6 6 6.4.5-4.9 4.2 1.5 6.3L10 14.6 4.4 18l1.5-6.3L1 7.5 7.4 7z" fill="#d32323"/></svg><svg class="star" viewBox="0 0 20 20"><path d="M10 1l2.6 6 6.4.5-4.9 4.2 1.5 6.3L10 14.6 4.4 18l1.5-6.3L1 7.5 7.4 7z" fill="#d32323"/></svg></div></div>
<div class="abs rating" style="left:764px"><span class="rating-name">Vastly</span><div class="stars"><svg class="star" viewBox="0 0 20 20"><path d="M10 1l2.6 6 6.4.5-4.9 4.2 1.5 6.3L10 14.6 4.4 18l1.5-6.3L1 7.5 7.4 7z" fill="#f2a712"/></svg><svg class="star" viewBox="0 0 20 20"><path d="M10 1l2.6 6 6.4.5-4.9 4.2 1.5 6.3L10 14.6 4.4 18l1.5-6.3L1 7.5 7.4 7z" fill="#f2a712"/></svg><svg class="star" viewBox="0 0 20 20"><path d="M10 1l2.6 6 6.4.5-4.9 4.2 1.5 6.3L10 14.6 4.4 18l1.5-6.3L1 7.5 7.4 7z" fill="#f2a712"/></svg><svg class="star" viewBox="0 0 20 20"><path d="M10 1l2.6 6 6.4.5-4.9 4.2 1.5 6.3L10 14.6 4.4 18l1.5-6.3L1 7.5 7.4 7z" fill="#f2a712"/></svg><svg class="star" viewBox="0 0 20 20"><path d="M10 1l2.6 6 6.4.5-4.9 4.2 1.5 6.3L10 14.6 4.4 18l1.5-6.3L1 7.5 7.4 7z" fill="#f2a712"/></svg></div></div>

<svg class="abs footer-curve" width="1200" height="90" viewBox="0 0 1200 90">
  <path d="M0 70 C400 90 800 70 1200 0 L1200 90 L0 90Z" fill="var(--purple)"/>
  <path d="M0 72 C400 96 800 84 1200 30 L1200 90 L0 90Z" fill="var(--green)"/>
</svg>
<footer class="abs footer">
  <div class="abs footer-col" style="left:163px">
    <h4>CONTACT US</h4>
    <ul>
      <li class="org">Ambermoor Wellness Centre</li>
      <li><svg class="ficon" viewBox="0 0 20 20"><circle cx="10" cy="10" r="9" fill="none" stroke="#fff" stroke-width="1.5"/><path d="M10 5a3 3 0 0 0-3 3c0 2.5 3 6 3 6s3-3.5 3-6a3 3 0 0 0-3-3z" fill="#fff"/></svg>48 Harlow Street East, Suite 210</li>
      <li style="padding-left:26px">Toronto, Ontario M4W 2K9</li>
      <li><svg class="ficon" viewBox="0 0 20 20"><circle cx="10" cy="10" r="9" fill="none" stroke="#fff" stroke-width="1.5"/><path d="M7 5l2 2-1 1.5c.6 1.4 1.6 2.4 3 3l1.5-1 2 2-1.5 1.5C9.5 14 6 10.5 5.5 6.5z" fill="#fff"/></svg>Phone: 416-555-0182</li>
      <li><svg class="ficon" viewBox="0 0 20 20"><circle cx="10" cy="10" r="9" fill="none" stroke="#fff" stroke-width="1.5"/><rect x="6" y="8" width="8" height="6" fill="none" stroke="#fff" stroke-width="1.3"/><rect x="7.5" y="5.5" width="5" height="3" fill="#fff"/></svg>Fax: 416-555-0176</li>
    </ul>
  </div>
  <div class="abs footer-col" style="left:475px">
    <h4>OPENING HOURS</h4>
    <ul><li>Mon - Fri: 7:30am - 8pm</li><li>Sat-Sun: 10am - 5pm</li></ul>
    <div class="social"><i></i><i></i><i></i><i></i><i></i></div>
  </div>
  <div class="abs footer-col" style="left:753px">
    <h4>OUR CENTRE</h4>
    <ul><li>&rsaquo; Home</li><li>&rsaquo; About Us</li><li>&rsaquo; Our Patients</li><li>&rsaquo; Why Us</li><li>&rsaquo; Blogs</li></ul>
  </div>
  <div class="abs footer-col" style="left:960px">
    <h4>RESOURCES</h4>
    <ul><li>&rsaquo; Our Services</li><li>&rsaquo; Testimonials</li><li>&rsaquo; Contact Us</li><li>&rsaquo; News</li></ul>
  </div>
</footer>
<div class="abs copyright">&copy; 2017 Ambermoor Wellness. All right reserved</div>

</body>
</html>
```